Fishing Tackle Product Packaging Backdrop/Template

Hi Designers,
we require a versatile packaging backdrop/template design for our fishing tackle brand. The design will be used in printed packaging for a range of products from small to large so would need to be scaleable. It will most commonly be used on small printed card tags (2x3"), but we would like to be able to use it for other packaging aswell.
A section for our product details, which we can edit ourselves would be essential, this way we can use the template for any of our products. The back of the card will need a space for our barcodes.
The design needs to be predominantly macsuline and appeal to the modern carp angler. It also needs to pop so that our goods really stand out against our competitors. Please see our logo attached. It'd also be great to see our web address at the bottom, on both sides of the design: www.pmriverside.co.uk

Thanks in advance and good luck!
PM Riverside Team

Target Market(s)

Male Carp Anglers (aprox ages 18-60)

Industry/Entity Type

Fishing Tackle

Requirements
Must have
• Our logo and web address, with a section for a barcode and product title/info

```html
<!DOCTYPE html>
<html lang="en">
<head>
<meta charset="utf-8">
<title>PM Riverside – Tackle Card Template</title>
<link rel="stylesheet" href="https://fonts.googleapis.com/css2?family=Roboto:wght@400;700;900&family=Roboto+Condensed:wght@700&display=swap">
<style>
  :root {
    --stage: #bfbfbf;
    --card-top: #3f600c;
    --card-mid: #2f4a08;
    --card-bottom: #1e3405;
    --gold: #f7c800;
    --gold-dark: #7a5a1a;
    --gold-mid: #c59a10;
    --gold-light: #ffd60a;
    --navy: #1b2366;
    --cream: #e8ecd8;
    --tagline: #3f6212;
    --fish-light: #7f9a45;
    --fish-mid: #5a7628;
    --fish-dark: #34501a;
    --angler: rgba(18, 32, 3, 0.35);
    --white: #ffffff;
  }
  * { box-sizing: border-box; margin: 0; padding: 0; }
  html, body { width: 1200px; height: 1000px; overflow: hidden; }
  body {
    background: var(--stage);
    font-family: "Roboto", Arial, sans-serif;
    position: relative;
  }
  .card {
    position: absolute;
    top: 138px;
    width: 482px;
    height: 724px;
    border-radius: 18px;
    overflow: hidden;
    background: linear-gradient(180deg, var(--card-top) 0%, var(--card-mid) 45%, var(--card-bottom) 100%);
  }
  .card--front { left: 85px; }
  .card--back { left: 633px; }

  /* illustration areas */
  .art { position: absolute; }
  .art--front-fish {
    left: -20px; top: 352px; width: 340px; height: 392px;
    border-radius: 0 62% 0 0 / 0 48% 0 0;
    background: linear-gradient(160deg, var(--fish-light) 0%, var(--fish-mid) 50%, var(--fish-dark) 100%);
  }
  .art--back-fish {
    left: 190px; top: -20px; width: 312px; height: 362px;
    border-radius: 0 0 0 70% / 0 0 0 60%;
    background: linear-gradient(200deg, var(--fish-light) 0%, var(--fish-mid) 50%, var(--fish-dark) 100%);
  }
  .art--angler {
    left: 15px; top: 333px; width: 267px; height: 391px;
    border-radius: 46% 46% 0 0 / 30% 30% 0 0;
    background: var(--angler);
  }

  .brand {
    position: absolute;
    top: 58px;
    display: flex;
    align-items: center;
    gap: 10px;
    color: var(--cream);
    font-weight: 700;
    font-size: 24px;
    white-space: nowrap;
  }
  .brand__dot {
    width: 34px; height: 34px;
    border-radius: 50%;
    background: var(--cream);
  }
  .card--front .brand { left: 50%; transform: translateX(-50%); }
  .card--back .brand { left: 26px; }

  .title-band {
    position: absolute;
    left: 0; top: 154px;
    width: 100%; height: 117px;
    border-top: 5px solid var(--navy);
    border-bottom: 5px solid var(--navy);
    background: linear-gradient(90deg, var(--gold-dark) 0%, var(--gold-mid) 15%, var(--gold-light) 50%, var(--gold-mid) 85%, var(--gold-dark) 100%);
  }
  .product-name {
    position: absolute;
    left: 87px; top: 18px;
    font-weight: 900;
    font-size: 40px;
    color: var(--navy);
    white-space: nowrap;
  }
  .feature-line {
    position: absolute;
    left: 87px; top: 63px;
    font-size: 22px;
    color: var(--navy);
  }
  .feature-rule {
    position: absolute;
    left: 245px; top: 85px;
    width: 148px; height: 2px;
    background: var(--navy);
  }

  .tagline {
    position: absolute;
    left: 271px; top: 614px;
    font-family: "Roboto Condensed", "Arial Narrow", sans-serif;
    font-weight: 700;
    font-size: 38px;
    line-height: 47px;
    color: var(--tagline);
  }

  .section-heading {
    position: absolute;
    left: 33px;
    font-weight: 700;
    font-size: 22px;
    color: var(--gold);
    white-space: nowrap;
  }
  .section-heading--description { top: 193px; }
  .section-heading--features { top: 349px; }
  .description {
    position: absolute;
    left: 33px; top: 218px;
    font-size: 16px;
    line-height: 25.8px;
    color: var(--gold);
    white-space: nowrap;
  }
  .feature-list {
    position: absolute;
    left: 33px; top: 374px;
    list-style: none;
    font-size: 17px;
    line-height: 20.5px;
    color: var(--gold);
  }
  .feature-list li { position: relative; padding-left: 25px; }
  .feature-list li::before {
    content: "";
    position: absolute;
    left: 1px; top: 5px;
    width: 10px; height: 10px;
    border-radius: 50%;
    background: var(--gold);
  }

  .barcode-area {
    position: absolute;
    left: 135px; top: 565px;
    width: 212px; height: 88px;
    border: 2px solid var(--white);
    padding: 3px;
  }
  .barcode-area__field { width: 100%; height: 100%; background: var(--white); }

  .web-address {
    position: absolute;
    left: 0; top: 669px;
    width: 480px;
    text-align: center;
    font-size: 20px;
    color: var(--white);
  }
</style>
</head>
<body>
  <section class="card card--front">
    <div class="art art--front-fish" role="img" aria-label="Illustration of a leaping carp in green tones"></div>
    <div class="brand"><span class="brand__dot"></span>PM Riverside</div>
    <div class="title-band">
      <h1 class="product-name">PRODUCT NAME</h1>
      <p class="feature-line">FEATURE LINE</p>
      <span class="feature-rule"></span>
    </div>
    <p class="tagline">Gear Up.<br>Catch More.</p>
  </section>

  <section class="card card--back">
    <div class="art art--back-fish" role="img" aria-label="Illustration of a carp leaping from the top corner"></div>
    <div class="art art--angler" role="img" aria-label="Faint silhouette of an angler holding a rod"></div>
    <div class="brand"><span class="brand__dot"></span>PM Riverside</div>
    <h2 class="section-heading section-heading--description">PRODUCT DESCRIPTION</h2>
    <p class="description">Lorem ipsum dolor sit amet consectetur<br>adipiscing elit. Dolor sit amet<br>consectetur adipiscing elit quisque<br>faucibus.</p>
    <h2 class="section-heading section-heading--features">KEY FEATURES</h2>
    <ul class="feature-list">
      <li>FEATURE 1</li>
      <li>FEATURE 2</li>
      <li>FEATURE 3</li>
      <li>FEATURE 4</li>
    </ul>
    <div class="barcode-area"><div class="barcode-area__field"></div></div>
    <p class="web-address">pmriverside.co.uk</p>
  </section>
</body>
</html>
```